Business Card for a mobile physiotherapy company

I need a layout for a business card for a mobile physiotherapy company.
Slogan is "Mobile Physiotherapy - Your Road To Recovery"
Phone number is 867-402-5913
Email VantrePhysio@mailbright.ca (subject to change with website)
Website www.VantrePhysio.ca
My name and credentials: Kent Vantre Kent Vantre, BSc(kin), MPT, CAFCI, IMS
Information maybe included: Direct Billing, Services including Physiotherapy, IMS, acupuncture
Maybe include facebook and instagram logos
One side with the logo clean and sharp
Other side with details, try not to look too busy, keep everything concise

```html
<!DOCTYPE html>
<html lang="en">
<head>
<meta charset="utf-8">
<title>Vantre Physio – Business Card</title>
<link href="https://fonts.googleapis.com/css2?family=Lato:ital,wght@0,400;0,700;0,900;1,400&family=Oswald:wght@600;700&display=swap" rel="stylesheet">
<style>
  :root {
    --page-bg: #eeece8;
    --card-blue: #4b6489;
    --card-white: #ffffff;
    --navy: #2c3f6b;
    --ink: #1f2a44;
    --rule: #5a6f96;
    --on-blue: #ffffff;
  }
  * { box-sizing: border-box; margin: 0; padding: 0; }
  html, body {
    width: 1200px; height: 1200px; overflow: hidden;
    background: var(--page-bg);
  }
  .canvas {
    position: relative; width: 1200px; height: 1200px;
    display: flex; flex-direction: column; align-items: center;
    justify-content: center; gap: 72px;
  }
  .card {
    position: relative; width: 900px; height: 514px;
    border-radius: 4px;
    box-shadow: 0 6px 18px rgba(0,0,0,0.12);
    overflow: hidden;
  }

  /* Logo side */
  .card--brand { background: var(--card-blue); color: var(--on-blue); }
  .brand-mark {
    position: absolute; left: 0; right: 0; top: 150px;
    text-align: center; font-family: "Lato", sans-serif; font-weight: 900;
    color: var(--on-blue);
  }
  .brand-mark__name { display: block; font-size: 104px; letter-spacing: 8px; line-height: 1; }
  .brand-mark__sub { display: block; font-size: 40px; letter-spacing: 30px; margin-top: 18px; padding-left: 30px; }
  .slogan {
    position: absolute; left: 0; right: 0; bottom: 44px; text-align: center;
    font-family: "Lato", sans-serif; font-size: 20px; font-style: italic;
    letter-spacing: 0.5px; color: var(--on-blue);
  }

  /* Details side */
  .card--details { background: var(--card-white); color: var(--ink); }
  .logo-name {
    position: absolute; right: 60px; top: 90px; text-align: right;
    font-family: "Lato", sans-serif; font-weight: 900; color: var(--navy);
  }
  .logo-name__main { display: block; font-size: 72px; letter-spacing: 6px; line-height: 1; }
  .logo-name__sub { display: block; font-size: 30px; letter-spacing: 22px; margin-top: 14px; margin-right: -22px; }

  .person { position: absolute; left: 90px; top: 236px; }
  .person__name {
    font-family: "Oswald", sans-serif; font-weight: 700; font-size: 46px;
    color: var(--navy); letter-spacing: 1px; line-height: 1.05;
  }
  .person__credentials {
    font-family: "Lato", sans-serif; font-size: 22px; color: var(--navy);
    margin-top: 4px;
  }
  .divider {
    position: absolute; left: 84px; right: 70px; top: 340px; height: 2px;
    background: linear-gradient(90deg, var(--navy) 0 40%, var(--rule) 40% 100%);
  }
  .contact-list {
    position: absolute; left: 88px; top: 356px; list-style: none;
    font-family: "Lato", sans-serif; font-size: 24px; color: var(--ink);
  }
  .contact-list li { display: flex; align-items: center; gap: 12px; height: 36px; }
  .contact-list svg { width: 18px; height: 18px; fill: var(--navy); flex: none; }
  .social {
    position: absolute; right: 74px; bottom: 48px; display: flex; align-items: center; gap: 12px;
    font-family: "Lato", sans-serif; font-size: 22px; color: var(--ink);
  }
  .social__square { width: 22px; height: 22px; background: var(--navy); border-radius: 3px; }
</style>
</head>
<body>
<main class="canvas">
  <section class="card card--brand" aria-label="Card front with logo">
    <div class="brand-mark">
      <span class="brand-mark__name">VANTRE</span>
      <span class="brand-mark__sub">PHYSIO</span>
    </div>
    <p class="slogan">“Mobile Physiotherapy - Your Road To Recovery”</p>
  </section>

  <section class="card card--details" aria-label="Card back with contact details">
    <div class="logo-name">
      <span class="logo-name__main">VANTRE</span>
      <span class="logo-name__sub">PHYSIO</span>
    </div>

    <div class="person">
      <h1 class="person__name">KENT VANTRE</h1>
      <p class="person__credentials">BSc(kin), MPT, CAFCI, IMS</p>
    </div>
    <div class="divider"></div>

    <ul class="contact-list">
      <li>
        <svg viewBox="0 0 24 24" aria-hidden="true"><path d="M6.6 10.8a15.1 15.1 0 0 0 6.6 6.6l2.2-2.2a1 1 0 0 1 1-.25 11.4 11.4 0 0 0 3.6.57 1 1 0 0 1 1 1V20a1 1 0 0 1-1 1A17 17 0 0 1 3 4a1 1 0 0 1 1-1h3.5a1 1 0 0 1 1 1c0 1.25.2 2.45.57 3.57a1 1 0 0 1-.25 1z"/></svg>
        867-402-5913
      </li>
      <li>
        <svg viewBox="0 0 24 24" aria-hidden="true"><path d="M2 5h20v14H2z M3.5 6.5 12 13l8.5-6.5" fill="none" stroke="#2c3f6b" stroke-width="2"/><path d="M2 5h20v2l-10 7L2 7z"/></svg>
        VantrePhysio@mailbright.ca
      </li>
      <li>
        <svg viewBox="0 0 24 24" aria-hidden="true"><circle cx="12" cy="12" r="9" fill="none" stroke="#2c3f6b" stroke-width="2"/><path d="M3 12h18M12 3c3 3 3 15 0 18M12 3c-3 3-3 15 0 18" fill="none" stroke="#2c3f6b" stroke-width="1.6"/></svg>
        www.VantrePhysio.ca
      </li>
    </ul>

    <div class="social">
      <span class="social__square" aria-hidden="true"></span>
      <span>@VantrePhysio</span>
    </div>
  </section>
</main>
</body>
</html>
```